Speisekarten-Design für persisches Restaurant
Zielgruppe
persisches Restaurant, möchte eine Karte mit schlichtem Design
Aufgabenstellung
bislang hatten wir ein Din A4 Karte mit vier Seiten. Kann gerne übernommen werden

```html
<!DOCTYPE html>
<html lang="de">
<head>
<meta charset="utf-8">
<title>Darvish – Speisekarte</title>
<link rel="stylesheet" href="https://fonts.googleapis.com/css2?family=Oswald:wght@400;500&family=Fira+Sans+Condensed:ital,wght@0,400;0,500;1,400&display=swap">
<style>
:root{
  --paper:#ffffff;
  --stage:#ffffff;
  --gold:#a8834f;
  --frame:#cdb89a;
  --ink:#2f2b29;
  --band:#3a3533;
  --badge:#9c7443;
}
*{box-sizing:border-box;margin:0;padding:0}
html,body{width:1200px;height:846px;overflow:hidden;background:var(--stage)}
.canvas{position:relative;width:1200px;height:846px}
.page{position:absolute;top:74px;width:494px;height:700px;background:var(--paper);box-shadow:0 1px 4px rgba(0,0,0,.18)}
.page--left{left:78px}
.page--right{left:624px}
.page__frame{position:absolute;inset:10px;border:1.5px solid var(--frame)}
.page__band{position:absolute;left:18px;right:18px;height:20px;background:var(--band)}
.page__band--top{top:18px}
.page__band--bottom{bottom:18px}

.section-title{position:absolute;left:26px;right:26px;display:flex;align-items:center;gap:8px;
  font-family:"Oswald",sans-serif;font-weight:400;font-size:15px;color:var(--ink);letter-spacing:.2px;white-space:nowrap}
.section-title::before,.section-title::after{content:"";flex:1;height:2px;background:var(--frame)}
.section-note{position:absolute;left:20px;right:20px;text-align:center;font-family:"Fira Sans Condensed",sans-serif;font-size:5.6px;color:var(--ink);line-height:14px}
.section-note em{font-style:italic}

.menu{position:absolute;display:grid;grid-template-columns:1fr 1fr;column-gap:12px}
.menu__col{display:flex;flex-direction:column}
.dish__head{display:flex;align-items:baseline;font-family:"Oswald",sans-serif;font-weight:500;font-size:10.5px;color:var(--gold);line-height:13px}
.dish__head sup{font-size:5px;margin-left:1px}
.dish__dots{flex:1;border-bottom:1.6px dotted var(--gold);margin:0 2px 3px}
.dish__de,.dish__en{font-family:"Fira Sans Condensed",sans-serif;font-size:5.6px;color:var(--ink);line-height:8.5px}
.dish__en{font-style:italic}

.badge{position:absolute;left:946px;top:308px;width:126px;height:126px;border-radius:50%;background:var(--badge);
  display:flex;flex-direction:column;align-items:center;justify-content:center;transform:rotate(-14deg);color:#fff;text-align:center}
.badge__title{font-family:"Oswald",sans-serif;font-size:13px;line-height:14px}
.badge__address{font-family:"Oswald",sans-serif;font-size:7.5px;line-height:9px;margin-top:4px}

.brand{position:absolute;left:821px;top:612px;width:100px;display:flex;flex-direction:column;align-items:center;gap:6px}
.brand__dot{width:44px;height:44px;border-radius:50%;background:var(--gold)}
.brand__name{font-family:"Oswald",sans-serif;font-weight:500;font-size:20px;color:var(--ink);letter-spacing:1px}
.brand__web{position:absolute;left:821px;width:100px;top:705px;text-align:center;font-family:"Oswald",sans-serif;font-weight:500;font-size:9px;color:var(--gold)}
</style>
</head>
<body>
<div class="canvas">

  <!-- Seite 3: Beilagen & Grill -->
  <section class="page page--left">
    <div class="page__frame"></div>
    <div class="page__band page__band--top" role="img" aria-label="Dunkles Zackenband als Seitenabschluss"></div>
    <div class="page__band page__band--bottom" role="img" aria-label="Dunkles Zackenband als Seitenabschluss"></div>

    <h2 class="section-title" style="top:62px">BEILAGEN &amp; EXTRAS // SIDE DISHES &amp; EXTRA</h2>
    <div class="menu" style="left:26px;right:29px;top:84px">
      <div class="menu__col" style="gap:9px">
        <div class="dish"><div class="dish__head">MASTO MUSIR<sup>G</sup><span class="dish__dots"></span>4,00</div><p class="dish__de">Joghurt mit wildem Knoblauch</p><p class="dish__en">Yoghurt with wild garlic</p></div>
        <div class="dish"><div class="dish__head">MASTO KHIAR<sup>G</sup><span class="dish__dots"></span>3,00</div><p class="dish__de">Joghurt mit Gurken und Minze</p><p class="dish__en">Yoghurt with cucumbers and peppermint</p></div>
        <div class="dish"><div class="dish__head">KHIAR SHOUR<span class="dish__dots"></span>3,00</div><p class="dish__de">Salzgurken nach persischer Art</p><p class="dish__en">Pickled cucumber, persian style</p></div>
        <div class="dish"><div class="dish__head">TORSHI<span class="dish__dots"></span>4,00</div><p class="dish__de">Sauer eingelegtes Gemüse</p><p class="dish__en">Sour pickled vegetables</p></div>
        <div class="dish"><div class="dish__head">SIR TORSHI<span class="dish__dots"></span>4,00</div><p class="dish__de">Eingelegter Knoblauch</p><p class="dish__en">Pickled garlic</p></div>
        <div class="dish"><div class="dish__head">BROT<span class="dish__dots"></span>0,70</div><p class="dish__en">Bread</p></div>
      </div>
      <div class="menu__col" style="gap:10.5px">
        <div class="dish"><div class="dish__head">BASMATIREIS<span class="dish__dots"></span>3,00</div><p class="dish__en">Basmati rice</p></div>
        <div class="dish"><div class="dish__head">BAGHALI POLO<span class="dish__dots"></span>4,50</div><p class="dish__en">Basmati rice with beans, dill tips and cinnamon</p></div>
        <div class="dish"><div class="dish__head">SERESHL POLO<span class="dish__dots"></span>4,50</div><p class="dish__en">Basmati rice with fried beans</p></div>
        <div class="dish"><div class="dish__head">SHIRIN POLO<sup>H</sup><span class="dish__dots"></span>5,00</div><p class="dish__en">Basmati rice with slivered almonds, chopped pistachios, orange peel and carrots</p></div>
        <div class="dish"><div class="dish__head">GRILLTOMATE<span class="dish__dots"></span>1,00</div><p class="dish__en">Grilled tomato</p></div>
        <div class="dish"><div class="dish__head">GEGRILLTES GEMÜSE<span class="dish__dots"></span>5,00</div><p class="dish__en">Grilled vegetables</p></div>
        <div class="dish"><div class="dish__head">BROT MIT SESAM<sup>K</sup><span class="dish__dots"></span>1,00</div><p class="dish__en">Bread with sesame</p></div>
        <div class="dish"><div class="dish__head">POMMES<span class="dish__dots"></span>3,50</div><p class="dish__en">Fries</p></div>
      </div>
    </div>

    <h2 class="section-title" style="top:361px">GRILLGERICHTE // GRILLED DISHES</h2>
    <p class="section-note" style="top:383px">Alle Grillgerichte werden mit Safran verfeinertem Basmatireis und Grilltomate serviert // <em>All grill dishes are served with saffron rice and grilled tomato</em><br>Alle Gerichte können auf Wunsch gegen 1,00 Aufpreis mit Baghali- oder Sereshk-Polo serviert werden // <em>All dishes are available also with Baghali- or Sereshk-Polo. Extra charge 1,00</em></p>
    <div class="menu" style="left:23px;right:29px;top:417px">
      <div class="menu__col" style="gap:11px">
        <div class="dish"><div class="dish__head">SOLTANI<span class="dish__dots"></span>20,00</div><p class="dish__de">Ein Spieß aus flach geklopftem Lammrücken und ein Lammhackfleischspieß</p><p class="dish__en">One skewer of lamb rack and one of lamb minced meat</p></div>
        <div class="dish"><div class="dish__head">KUBIDEH<span class="dish__dots"></span>14,00</div><p class="dish__de">Zwei Lammhackfleischspieße</p><p class="dish__en">Two skewers of lamb minced meat</p></div>
        <div class="dish"><div class="dish__head">DJUDJE<sup>G</sup><span class="dish__dots"></span>14,00</div><p class="dish__de">Ein Spieß aus Hähnchenbrust-Stücken</p><p class="dish__en">One skewer of chicken breast pieces</p></div>
        <div class="dish"><div class="dish__head">SHISHLIK<span class="dish__dots"></span>19,00</div><p class="dish__de">Gegrillte Lammkarree-Stücke</p><p class="dish__en">Grilled lamb chops</p></div>
      </div>
      <div class="menu__col" style="gap:11px">
        <div class="dish"><div class="dish__head">BARG<span class="dish__dots"></span>16,00</div><p class="dish__de">Ein Spieß aus flach geklopftem Lammrücken</p><p class="dish__en">One skewer of lamb rack</p></div>
        <div class="dish"><div class="dish__head">CHENJE<span class="dish__dots"></span>16,00</div><p class="dish__de">Ein Spieß aus Lammfilet-Stücken</p><p class="dish__en">One skewer of lamb fillet pieces</p></div>
        <div class="dish"><div class="dish__head">DJUDJE SOLTANI<sup>G</sup><span class="dish__dots"></span>18,00</div><p class="dish__de">Ein Spieß aus Hähnchenbrust-Stücken und ein Lammhackfleischspieß</p><p class="dish__en">One skewer of chicken breast pieces and one of lamb minced meat</p></div>
        <div class="dish"><div class="dish__head">BAKHTIARI<sup>G</sup><span class="dish__dots"></span>16,00</div><p class="dish__de">Ein gemischter Spieß aus Lammfilet- und Hähnchenbrust-Stücken</p><p class="dish__en">One mixed skewer of lamb fillet and chicken breast pieces</p></div>
      </div>
    </div>
  </section>

  <!-- Seite 4: Schmorgerichte -->
  <section class="page page--right">
    <div class="page__frame"></div>
    <div class="page__band page__band--top" role="img" aria-label="Dunkles Zackenband als Seitenabschluss"></div>
    <div class="page__band page__band--bottom" role="img" aria-label="Dunkles Zackenband als Seitenabschluss"></div>

    <h2 class="section-title" style="top:62px">SCHMORGERICHTE // BRAISED DISHES</h2>
    <p class="section-note" style="top:79px">Alle Schmorgerichte werden mit Safran verfeinertem Basmatireis serviert // <em>All braised dishes are served with saffron basmati rice</em></p>
    <div class="menu" style="left:27px;right:26px;top:104px">
      <div class="menu__col" style="gap:11px">
        <div class="dish"><div class="dish__head">GHORME SABSI<span class="dish__dots"></span>14,00</div><p class="dish__de">Gericht mit Fleischstücken aus der Lammkeule, Bohnen, Limette und verschiedenen Kräutern (Schnittlauch, Petersilie, Bockshornklee)</p><p class="dish__en">Sauce made from pieces of meat from leg of lamb, beans, lemon and various herbs (chives, parsley, fenugreek)</p></div>
        <div class="dish"><div class="dish__head">BADEMJAN<span class="dish__dots"></span>15,00</div><p class="dish__de">Gericht mit Fleischstücken aus der Lammkeule und Auberginen</p><p class="dish__en">Sauce made from pieces of meat from leg of lamb and aubergines</p></div>
      </div>
      <div class="menu__col" style="gap:11px">
        <div class="dish"><div class="dish__head">GHEIMEH BADEMJAN<span class="dish__dots"></span>15,00</div><p class="dish__de">Gericht mit Fleischstücken aus der Lammkeule, Auberginen und Linsen</p><p class="dish__en">Sauce made from pieces of meat from leg of lamb, aubergines and lentil</p></div>
        <div class="dish"><div class="dish__head">BAMIEH<span class="dish__dots"></span>15,00</div><p class="dish__de">Gericht mit Fleischstücken aus der Lammkeule und Okraschoten</p><p class="dish__en">Sauce made from pieces of meat from leg of lamb and okras</p></div>
      </div>
    </div>
  </section>

  <div class="badge">
    <p class="badge__title">WIR FREUEN UNS<br>AUF IHREN BESUCH!</p>
    <p class="badge__address">Lindenallee 24<br>60311 Musterstadt</p>
  </div>

  <div class="brand">
    <span class="brand__dot"></span>
    <span class="brand__name">DARVISH</span>
  </div>
  <p class="brand__web">WWW.DARVISH-KUECHE.DE</p>

</div>
</body>
</html>
```